Letterhead Design Project

Based on the attached logo we would like have a designed of stationary.
As we are a management consulting company focused on business development dealing with C-level and one level below we new business cards.
We have decided to use HGP (Harbor Growth Partners) as the business name. The legal name will be Harbor Growth Partners ApS but we will brand us under HGP. The tack line is “Shaping Steady Gains” if we need one.
For legal reasons we need to have the legal name on the letters together with the company no. (cvr. nr. 58197024)
We want to signal the following:
- Serious
- Professional
- Creating Result
- Capable of thinking out of the box and creative
- Fast reactions we will be there when needed
What we do not want to be view as is:
- To smart
- We know better
- We can fix it yesterday
Our Value Proposition is two sited:
- Increasing revenue
- Reduced sales cost or increased efficiency
Therefore, companies can call us when they want to grow or they need to be more efficient.
Our business cards should have a two sided print with the logo incl. the tack line on one side and the detailed information on the other site.
We need to have the following information on the letter head:
- Legal company name
- Cvr nr.
- Address incl. country name (Denmark)
- Main number
- Wed address
Symbols are welcome to be used to guide for the above information.
The following information are expected to be in the personal signature of the letter.
- Name
- Title
- Mobile number
- E-mail address
Updates
Some of you has requested our specific details so here they come:
- Address incl. country name (Denmark): Lyngvejen 42, 4790 Solvange, Denmark
- Main number: +45 5871 3302
- Wed address: www.hgprises.example
Mobile no. are +45 xxxx xxxx or +45 4390 1256
Our e-mail looks like this: firstname.seconname@KLMRISES.EXAMPLE or for me: jonas.halvorsen@klmrises.example
We need the design (file) as finish as posible so we just need to add personal details before printing.
Please be aware that we will prefer designs where we can print the full letter incl. design. As we are communicating on e-mails with pdf versions of the letter we also need to have a design which will print on the clients printers.
Target Market(s)
C level and one level below.
Major local and international Companies.
Industry/Entity Type
Management Consulting
Font styles to use
Colors
Designer to choose colors to be used in the design.
Requirements
Must have
- Use of our logo without tack line

```html
<!DOCTYPE html>
<html lang="en">
<head>
<meta charset="utf-8">
<title>HGP Stationery</title>
<link href="https://fonts.googleapis.com/css2?family=Questrial&display=swap" rel="stylesheet">
<style>
  :root {
    --backdrop: #bdbdbd;
    --paper: #f7f7f7;
    --paper-edge: #e4e4e4;
    --brand: #1a6fc0;
    --brand-light: #2b8fd6;
    --brand-dark: #0b5aab;
    --ink: #4a4a4a;
    --rule: #9a9a9a;
  }
  * { margin: 0; padding: 0; box-sizing: border-box; }
  html, body { width: 1200px; height: 800px; overflow: hidden; }
  body {
    background: var(--backdrop);
    font-family: "Questrial", sans-serif;
    color: var(--ink);
    position: relative;
  }
  .sheet {
    position: absolute;
    background: var(--paper);
    border: 1px solid var(--paper-edge);
    box-shadow: 0 2px 6px rgba(0,0,0,0.12);
  }
  .brand-stripe {
    position: absolute; left: 0; right: 0; top: 0; height: 7px;
    background: linear-gradient(90deg, var(--brand-light), var(--brand-dark));
  }
  .wordmark {
    position: absolute;
    font-family: "Questrial", sans-serif;
    color: var(--brand);
    letter-spacing: 1px;
    line-height: 1;
    white-space: nowrap;
  }
  .web { white-space: nowrap; }
  .web strong { color: var(--brand); font-weight: 400; }

  /* Envelope, open back */
  .envelope-open { left: 120px; top: 68px; width: 470px; height: 400px; border-radius: 10px 10px 0 0; }
  .envelope-open .liner {
    position: absolute; left: 0; right: 0; top: 0; height: 100px;
    background: linear-gradient(180deg, #ececec, #f2f2f2);
    border-radius: 10px 10px 0 0;
  }
  .envelope-open .liner-throat {
    position: absolute; left: 20px; right: 20px; top: 100px; height: 50px;
    background: linear-gradient(180deg, #ececec, var(--paper));
  }

  /* Envelope, back with blue flap */
  .envelope-flap { left: 132px; top: 295px; width: 463px; height: 240px; }
  .envelope-flap .flap {
    position: absolute; left: 4px; right: 0; top: -2px; height: 76px;
    background: linear-gradient(90deg, var(--brand-light), var(--brand-dark));
    border-radius: 0 0 14px 14px;
  }
  .envelope-flap .flap .wordmark {
    color: rgba(255,255,255,0.55);
    font-size: 14px; left: 50%; top: 28px; transform: translateX(-50%);
  }

  /* Envelope, front */
  .envelope-front { left: 82px; top: 485px; width: 455px; height: 235px; }
  .envelope-front .wordmark { left: 38px; top: 44px; font-size: 44px; }
  .envelope-front .legal-name { position: absolute; left: 38px; top: 177px; font-size: 7.5px; white-space: nowrap; }
  .envelope-front .rule { position: absolute; left: 38px; right: 32px; top: 190px; height: 3px; border-top: 1px solid var(--rule); border-bottom: 1px solid #d0d0d0; }
  .envelope-front .address { position: absolute; left: 38px; top: 203px; font-size: 6.5px; white-space: nowrap; }
  .envelope-front .web { position: absolute; right: 32px; top: 199px; font-size: 8px; }

  /* Letterhead */
  .letterhead { left: 652px; top: 92px; width: 488px; height: 650px; }
  .letterhead .wordmark { right: 66px; top: 88px; font-size: 42px; }
  .letterhead .legal-name { position: absolute; left: 26px; top: 548px; font-size: 7.5px; white-space: nowrap; }
  .letterhead .contact { position: absolute; left: 26px; top: 574px; font-size: 6.5px; white-space: nowrap; }
  .letterhead .contact b { color: var(--brand); font-weight: 400; }
  .letterhead .rule-bottom { position: absolute; left: 26px; right: 88px; top: 594px; height: 3px; border-top: 1px solid var(--rule); border-bottom: 1px solid #d0d0d0; }
  .letterhead .web { position: absolute; right: 88px; top: 604px; font-size: 8px; }
</style>
</head>
<body>

  <section class="sheet envelope-open" aria-label="Envelope, open back">
    <div class="liner" role="img" aria-label="Envelope liner with a faint repeated pattern"></div>
    <div class="liner-throat"></div>
  </section>

  <section class="sheet envelope-flap" aria-label="Envelope, back with flap">
    <div class="flap"><span class="wordmark">HGP</span></div>
  </section>

  <section class="sheet envelope-front" aria-label="Envelope, front">
    <div class="brand-stripe"></div>
    <span class="wordmark">HGP</span>
    <p class="legal-name">Harbor Growth Partners ApS</p>
    <div class="rule"></div>
    <p class="address">Lyngvejen 42, 4790 Solvange, Denmark</p>
    <p class="web"><strong>www.hgprises.example</strong></p>
  </section>

  <section class="sheet letterhead" aria-label="Letterhead">
    <div class="brand-stripe"></div>
    <span class="wordmark">HGP</span>
    <p class="legal-name">Harbor Growth Partners ApS</p>
    <p class="contact">Lyngvejen 42, 4790 Solvange, Denmark · <b>T:</b> +45 4390 1256 · <b>E:</b> info@hgprises.example · Company Nr: 58197024</p>
    <div class="rule-bottom"></div>
    <p class="web"><strong>www.hgprises.example</strong></p>
  </section>

</body>
</html>
```